Pharmacy

Two sided postcard. Pictures on one side. Description on the other. We design and build pharmacies. pictures are some of our finished work. You can use as many pictures as you like not necessary to use all of them. Size of card should be 5"x7". See my website at display@brightfieldfixtures.com for more inspiration. I include the back of one card that I used recently. Both sids need design input. Feel free to contact me with questions.
Requirements
Must have
- Must be a two sided postcard
Nice to have
- I am sending a design of a sleek type postcard that I saw online as an example.
- https://lnk.example-pics.net/images/q7KmRz
- I am looking for something modern.
- Not limited to colors on my website.

```html
<!DOCTYPE html>
<html lang="en">
<head>
<meta charset="utf-8">
<title>Brightfield Showcase &amp; Store Fixture – Postcard</title>
<link rel="stylesheet" href="https://fonts.googleapis.com/css2?family=Roboto+Condensed:wght@700&family=Open+Sans:wght@300;400;600;700&display=swap">
<style>
  :root{
    --stage:#323232;
    --red-dark:#8e0000;
    --red:#c40d0d;
    --red-deep:#a30505;
    --blue:#0a44b4;
    --white:#ffffff;
    --ink:#111111;
    --stamp:#e6e6e6;
  }
  *{margin:0;padding:0;box-sizing:border-box}
  html,body{width:1200px;height:1200px;overflow:hidden;background:var(--stage)}
  body{position:relative;font-family:"Open Sans",sans-serif}

  .card{position:absolute;width:668px;height:477px;background:var(--white);overflow:hidden}
  .card--front{left:103px;top:84px}
  .card--back{left:429px;top:608px}

  /* front */
  .front-panel{position:absolute;left:0;top:0;width:252px;height:400px;
    background:linear-gradient(90deg,var(--red) 0%,var(--red-deep) 70%,var(--red-dark) 100%)}
  .front-title{position:absolute;left:21px;top:22px;color:var(--white);
    font-family:"Roboto Condensed",sans-serif;font-weight:700;font-size:39px;line-height:37px;letter-spacing:-.3px}
  .front-rule{position:absolute;left:22px;top:182px;width:235px;height:1px;
    background:linear-gradient(90deg,rgba(255,255,255,.7),rgba(255,255,255,.05))}
  .front-intro{position:absolute;left:23px;top:194px;color:var(--white);font-weight:600;font-size:17px;line-height:22px}
  .service-list{position:absolute;left:23px;top:235px;list-style:none;color:var(--white);font-weight:700;font-size:16px}
  .service-list li{display:flex;align-items:center;height:30.5px}
  .service-list svg{width:13px;height:13px;margin-right:11px;flex:none}

  .hero-photo{position:absolute;left:252px;top:0;width:416px;height:352px;
    background:linear-gradient(180deg,#d6cfc6 0%,#c99d7e 30%,#7b4b33 55%,#9a8b86 72%,#5a3b2e 100%)}
  .thumb{position:absolute;border:3px solid var(--white);box-shadow:0 1px 4px rgba(0,0,0,.35)}
  .thumb--f1{left:211px;top:300px;width:135px;height:90px;background:linear-gradient(135deg,#6e3a25,#c8b9a4 55%,#7b4733)}
  .thumb--f2{left:365px;top:300px;width:135px;height:90px;background:linear-gradient(135deg,#e7ddd0,#8a5a3c 50%,#cdbfa8)}
  .thumb--f3{left:519px;top:300px;width:135px;height:90px;background:linear-gradient(135deg,#3f4a63,#a9a39a 50%,#5a5f78)}

  .front-web{position:absolute;left:0;top:400px;width:252px;height:77px;display:flex;align-items:center;padding-left:21px;
    font-size:15px;font-style:italic;color:var(--ink);letter-spacing:-.4px}
  .front-web svg{width:9px;height:9px;margin-right:8px}
  .front-contact{position:absolute;left:252px;top:400px;width:416px;height:77px;background:var(--blue);color:var(--white);padding:11px 0 0 27px}
  .front-contact .call{font-size:26px;line-height:30px}
  .front-contact .call b,.front-contact .mail b{font-weight:700}
  .front-contact .mail{font-size:15px;line-height:20px}

  /* back */
  .back-panel{position:absolute;left:0;top:0;width:371px;height:477px;
    background:linear-gradient(180deg,var(--red) 0%,var(--red-deep) 40%,#c23a3a 62%,#eec6c6 80%,#fbf1f1 100%)}
  .back-title{position:absolute;left:22px;top:22px;color:var(--white);
    font-family:"Roboto Condensed",sans-serif;font-weight:700;font-size:29px;line-height:29px;letter-spacing:-.2px}
  .tagline{position:absolute;left:17px;top:90px;width:338px;height:26px;border-radius:13px;background:var(--blue);
    color:var(--white);font-weight:700;font-size:19px;line-height:26px;text-align:center}
  .about{position:absolute;left:23px;top:123px;width:326px;color:var(--white);font-weight:300;font-size:12.4px;line-height:16px;letter-spacing:-.15px;text-align:justify}
  .thumb--b1{left:22px;top:241px;width:161px;height:117px;background:linear-gradient(135deg,#b28a6c,#e9e1d4 45%,#2a2a2a 75%,#7d4a30)}
  .thumb--b2{left:198px;top:241px;width:161px;height:117px;background:linear-gradient(135deg,#5c3d2e,#c8c0b6 50%,#7a4630)}
  .back-call{position:absolute;left:0;top:371px;width:371px;text-align:center;color:var(--red-deep);font-size:24px;line-height:30px}
  .back-call b{color:var(--ink);font-weight:700}
  .back-contact{position:absolute;left:0;top:408px;width:371px;height:46px;background:var(--blue);color:var(--white);
    font-size:15px;line-height:18px;text-align:center;padding-top:5px}
  .back-contact svg{width:11px;height:9px;margin-right:6px;vertical-align:-1px}

  .mailing{position:absolute;left:382px;top:28px;font-size:12px;line-height:18px;color:var(--ink);font-style:normal}
  .mailing .name{font-weight:600}
  .stamp{position:absolute;left:594px;top:22px;width:51px;height:55px;background:var(--stamp)}
</style>
</head>
<body>

<section class="card card--front">
  <div class="hero-photo" role="img" aria-label="Photo of a finished pharmacy interior with wooden shelving and glass display counters"></div>
  <div class="front-panel">
    <h1 class="front-title">Brightfield<br>Showcase &amp;<br>Store Fixture<br>co Inc.</h1>
    <div class="front-rule"></div>
    <p class="front-intro">A Complete Service From<br>Design Thru Installation</p>
    <ul class="service-list">
      <li><svg viewBox="0 0 16 16"><circle cx="8" cy="8" r="8" fill="#fff"/><path d="M4.5 8.3l2.3 2.3 4.7-4.8" stroke="#b30808" stroke-width="2" fill="none"/></svg>Pharmacies</li>
      <li><svg viewBox="0 0 16 16"><circle cx="8" cy="8" r="8" fill="#fff"/><path d="M4.5 8.3l2.3 2.3 4.7-4.8" stroke="#b30808" stroke-width="2" fill="none"/></svg>Jewelry Stores</li>
      <li><svg viewBox="0 0 16 16"><circle cx="8" cy="8" r="8" fill="#fff"/><path d="M4.5 8.3l2.3 2.3 4.7-4.8" stroke="#b30808" stroke-width="2" fill="none"/></svg>Vintage Stores</li>
      <li><svg viewBox="0 0 16 16"><circle cx="8" cy="8" r="8" fill="#fff"/><path d="M4.5 8.3l2.3 2.3 4.7-4.8" stroke="#b30808" stroke-width="2" fill="none"/></svg>Other Stores</li>
      <li><svg viewBox="0 0 16 16"><circle cx="8" cy="8" r="8" fill="#fff"/><path d="M4.5 8.3l2.3 2.3 4.7-4.8" stroke="#b30808" stroke-width="2" fill="none"/></svg>Prefabricated</li>
    </ul>
  </div>
  <div class="thumb thumb--f1" role="img" aria-label="Photo of pharmacy wall shelving stocked with products"></div>
  <div class="thumb thumb--f2" role="img" aria-label="Photo of a curved pharmacy shelving unit"></div>
  <div class="thumb thumb--f3" role="img" aria-label="Photo of a store aisle with display fixtures"></div>
  <div class="front-web">
    <svg viewBox="0 0 10 10"><circle cx="5" cy="5" r="4.3" fill="none" stroke="#c40d0d" stroke-width="1.2"/><path d="M.7 5h8.6M5 .7v8.6" stroke="#c40d0d" stroke-width="1"/></svg>
    www.brightfieldfixtures.com
  </div>
  <div class="front-contact">
    <p class="call">Give us a call at <b>201 555 0148</b></p>
    <p class="mail">or email at : <b>display@brightfieldfixtures.com</b></p>
  </div>
</section>

<section class="card card--back">
  <div class="back-panel">
    <h2 class="back-title">Brightfield Showcase &amp; Store<br>Fixture co. Inc.</h2>
    <p class="tagline">Quality - Experience - Innovation</p>
    <p class="about">Family owned and operated for three generations Brightfield Showcase &amp; Store Fixture Co. Inc is the oldest store fixture company in New Jersey As designers &amp; Manufacturers we can save you hours of time and money. Our level of experience will be evident from the outset and you will be pleased that you found us.</p>
    <div class="thumb thumb--b1" role="img" aria-label="Photo of a pharmacy checkout counter with checkered floor"></div>
    <div class="thumb thumb--b2" role="img" aria-label="Photo of a pharmacy counter with product shelving behind"></div>
    <p class="back-call">Give us a call at: <b>201 555 0148</b></p>
    <div class="back-contact">
      <div><svg viewBox="0 0 12 9"><rect x=".5" y=".5" width="11" height="8" fill="#fff"/><path d="M.5 .5L6 5l5.5-4.5" stroke="#0a44b4" fill="none"/></svg>display@brightfieldfixtures.com</div>
      <div><svg viewBox="0 0 10 10"><circle cx="5" cy="5" r="4.3" fill="none" stroke="#fff" stroke-width="1.2"/><path d="M.7 5h8.6M5 .7v8.6" stroke="#fff" stroke-width="1"/></svg>www.brightfieldfixtures.com</div>
    </div>
  </div>
  <address class="mailing">
    <div class="name">Brightfield showcase<br>&amp; Store Fixture Co. Inc.</div>
    <div>PO Box 318<br>Fairhaven NJ 07704</div>
  </address>
  <div class="stamp"></div>
</section>

</body>
</html>
```